New PowerPoint Design Project

A well-known speaker needs a visual presence that compliments his amazing, consistent performance onstage. You'll easily improve this deck, and I'll leave it to you whether you stick with the palette defined by the original BLQEMS icons you'll find in the deck, the mishmosh in the deck as it stands, OR get extra points by going with the corporate color palette so our speaking slides fit with Ronan's brands and his three sub-brands. A look at the Ronan subbrand .png in the attached zip file might give you some ideas.
Updates

Just noting that I'm available to answer questions or supply assets you think you'd need. The big design issue I'm looking for someone to solve is how you'll treat the bright clusters of icons in information graphics of the deck.

Target Market(s)

Corporate Executives and wanabees

Requirements
Must have
• The footer needs to have the Dellwyn Bluepath logo and Twitter and Facebook link and you need to do the first 27 slides. The slides past 27 are there simply if you want to use assets from those slides.
Nice to have
• Use the palette document in the zip rather than palette dictated by the BLQEMS icons in the deck (I do not have source for the icons.).

```html
<!DOCTYPE html>
<html lang="en">
<head>
<meta charset="utf-8">
<title>Aligned Purpose</title>
<link rel="stylesheet" href="https://fonts.googleapis.com/css2?family=Open+Sans:ital,wght@0,400;0,600;0,700;1,700&display=swap">
<style>
  :root {
    --ink: #111111;
    --leaf: #8dc63f;
    --axis: #f2e24a;
    --white: #ffffff;
    --teal: #13a9b6;
    --red: #e52b2b;
    --blue: #1d6fb4;
    --gold: #fcc717;
  }
  html, body { margin: 0; padding: 0; overflow: hidden; background: var(--ink); }
  .slide {
    position: relative; width: 1200px; height: 674px; overflow: hidden;
    background: var(--leaf); font-family: "Open Sans", Arial, sans-serif;
  }
  .side-panel { position: absolute; left: 0; top: 0; width: 380px; height: 674px; background: var(--ink); }
  .slide-title {
    position: absolute; left: 31px; top: 272px; margin: 0;
    color: var(--leaf); font-weight: 400; font-size: 44px; line-height: 56px; letter-spacing: 0.5px;
  }
  .diagram { position: absolute; left: 0; top: 0; }
  .axis-label {
    position: absolute; color: var(--white); font-size: 13px; font-weight: 700; font-style: italic; letter-spacing: 0.3px;
  }
  .stage-label { position: absolute; color: var(--white); font-size: 21px; font-weight: 600; line-height: 28px; }
  .footer-brand {
    position: absolute; left: 17px; top: 643px; display: flex; align-items: center; gap: 8px;
    color: var(--white); font-size: 22px; font-weight: 400; line-height: 28px;
  }
  .footer-brand .mark { width: 20px; height: 20px; background: var(--white); }
  .footer-note { position: absolute; top: 649px; color: var(--ink); font-size: 15px; line-height: 20px; }
</style>
</head>
<body>
<div class="slide">
  <div class="side-panel"></div>
  <h1 class="slide-title">ALIGNED<br>PURPOSE</h1>

  <svg class="diagram" width="1200" height="674" viewBox="0 0 1200 674">
    <g class="advance-badge">
      <circle cx="380" cy="316" r="57" fill="var(--ink)" stroke="var(--leaf)" stroke-width="3"/>
      <path d="M350 298 L368 316 L350 334 L360 334 L378 316 L360 298 Z" fill="var(--leaf)"/>
      <path d="M373 298 L391 316 L373 334 L383 334 L401 316 L383 298 Z" fill="var(--leaf)"/>
    </g>
    <g class="axes" stroke="var(--axis)" stroke-width="2" fill="none">
      <line x1="484" y1="566" x2="484" y2="76"/>
      <polyline points="476,86 484,74 492,86"/>
      <line x1="462" y1="551" x2="1174" y2="551"/>
      <polyline points="1164,543 1176,551 1164,559"/>
    </g>
    <g class="stages">
      <circle cx="541" cy="462" r="41" fill="var(--teal)" role="img" aria-label="Icon: person raising a hand"/>
      <circle cx="661" cy="378" r="41" fill="var(--red)" role="img" aria-label="Icon: person with signal waves"/>
      <circle cx="768" cy="299" r="41" fill="var(--blue)" role="img" aria-label="Icon: arrows branching outward"/>
      <circle cx="866" cy="206" r="41" fill="var(--gold)" role="img" aria-label="Icon: pointing hand"/>
      <circle cx="994" cy="126" r="41" fill="var(--teal)" role="img" aria-label="Icon: adult standing with a child"/>
    </g>
  </svg>

  <span class="axis-label" style="left:438px;top:44px;">EMOTIONAL</span>
  <span class="axis-label" style="left:398px;top:515px;">EXTERNAL</span>
  <span class="axis-label" style="left:1089px;top:522px;">INTERNAL</span>
  <span class="axis-label" style="left:438px;top:582px;">INTELLECTUAL</span>

  <span class="stage-label" style="left:619px;top:460px;">I said so</span>
  <span class="stage-label" style="left:720px;top:383px;">Makes Sense</span>
  <span class="stage-label" style="left:827px;top:299px;">Mission Driven</span>
  <span class="stage-label" style="left:938px;top:206px;">Your Stuff</span>
  <span class="stage-label" style="left:1054px;top:110px;">Belonging</span>

  <div class="footer-brand"><span class="mark"></span><span>dellwynbluepath</span></div>
  <span class="footer-note" style="left:456px;">COPYRIGHT 2013</span>
  <span class="footer-note" style="left:746px;">@dellwyn</span>
  <span class="footer-note" style="left:1044px;">/Ronandellwyn</span>
</div>
</body>
</html>
```